Corwen Physical Therapy Website

I would need a clean modern website built to showcase my Physical therapy brand and services. I would need a simple but descriptive website that can ultimately connect my patients to my electronic medical portal so they may book an appointment..

```html
<!DOCTYPE html>
<html lang="en">
<head>
<meta charset="utf-8">
<title>Corwen Physical Therapy</title>
<link href="https://fonts.googleapis.com/css2?family=Krona+One&family=Roboto:wght@400;500;700&display=swap" rel="stylesheet">
<style>
:root{
  --teal:#2a8c84;
  --teal-dark:#1f6f69;
  --green:#7cc04a;
  --green-dark:#3e8e1f;
  --purple:#6a50b2;
  --ink:#1d1d1d;
  --grey:#777;
  --footer:#323232;
  --field:#cfe3e0;
}
*{margin:0;padding:0;box-sizing:border-box}
html,body{width:1200px;height:4387px;overflow:hidden;background:#fff}
body{font-family:'Roboto',Arial,sans-serif;color:var(--ink)}
.page{position:relative;width:1200px;height:4387px;overflow:hidden}
.abs{position:absolute}
.display{font-family:'Krona One','Arial Black',sans-serif;letter-spacing:3px}

/* top bar & nav */
.topbar{top:0;left:0;width:1200px;height:43px;background:#fff;border-bottom:1px solid #eee}
.topbar ul{position:absolute;right:115px;top:14px;list-style:none;display:flex;font-size:11px;font-weight:700}
.topbar li+li:before{content:"|";margin:0 8px;font-weight:400}
.navbar{top:43px;left:0;width:1200px;height:88px;background:#fff}
.logo-badge{top:40px;left:108px;width:130px;height:130px;border-radius:50%;background:#fff;z-index:3;display:flex;align-items:center;justify-content:center;flex-direction:column}
.logo-badge .dot{width:34px;height:34px;border-radius:50%;background:var(--teal);margin-bottom:6px}
.logo-badge span{font-weight:700;font-size:16px;color:var(--teal-dark)}
.mainnav{left:335px;top:81px;display:flex;gap:24px;font-size:12px;font-weight:500;list-style:none}
.btn-appoint{left:880px;top:66px;width:206px;height:44px;background:var(--teal);color:#fff;font-size:12px;font-weight:500;display:flex;align-items:center;justify-content:center}

/* hero */
.hero{top:131px;left:0;width:1200px;height:557px;background:linear-gradient(90deg,#8fa2ad 0%,#c9d3d8 35%,#e6eaec 60%,#f1f2f3 100%)}
.hero-title{left:668px;top:270px;font-size:54px;color:#111;letter-spacing:6px}
.hero-sub{left:668px;top:346px;font-size:30px;line-height:38px;color:#111;letter-spacing:3px}
.hero-text{left:668px;top:432px;width:430px;font-size:13px;line-height:22px;color:#333}
.btn{background:var(--teal);color:#fff;font-size:12px;font-weight:700;display:flex;align-items:center;justify-content:center;gap:8px}
.btn .arr{width:14px;height:14px;border-radius:50%;background:#fff;position:relative}
.btn .arr:after{content:"";position:absolute;left:4px;top:4px;border-left:6px solid var(--teal);border-top:3px solid transparent;border-bottom:3px solid transparent}
.btn.green{background:var(--green)}
.btn.green .arr:after{border-left-color:var(--green)}

/* features */
.feature{top:810px;width:235px;height:263px;color:#fff;text-align:center;padding-top:30px}
.feature svg{display:block;margin:0 auto}
.feature h3{font-size:13px;font-weight:700;margin-top:26px}
.feature hr{width:32px;border:0;border-top:2px solid #fff;margin:12px auto}
.feature p{font-size:12.5px;line-height:22px;padding:0 22px}

/* about */
.about{top:1191px;left:0;width:1200px;height:471px;background:var(--teal)}
.about h2{left:150px;top:1251px;font-size:29px;color:#fff}
.about-text{left:150px;top:1308px;width:460px;font-size:12.5px;line-height:24px;color:#e6f2f0;text-align:justify}
.about-photo{left:679px;top:1243px;width:370px;height:370px;border-radius:50%;background:radial-gradient(circle at 50% 40%,#f3f1ea,#c7cbbd 70%,#9da794);border:6px solid #fff}

/* section headings */
.sec-title{width:1200px;left:0;text-align:center;font-size:29px;color:#111}

/* services */
.svc-img{top:1834px;width:478px;height:316px}
.svc-title{top:2157px;width:478px;text-align:center;font-size:23px}
.svc-text{top:2215px;width:478px;text-align:center;font-size:13px;line-height:24px;color:var(--grey);padding:0 40px}
.link{font-size:11.5px;font-weight:700;color:var(--teal);text-decoration:underline}

/* testimonials */
.testi{top:2442px;left:0;width:1200px;height:359px;background:linear-gradient(90deg,#3e4144 0%,#55585c 50%,#5f6367 100%)}
.testi h2{left:112px;top:2532px;font-size:30px;line-height:38px;color:#fff}
.testi-lead{left:112px;top:2612px;width:300px;font-size:14px;line-height:24px;color:#f1f1f1}
.testi-photo{left:452px;top:2520px;width:172px;height:195px;border:3px solid #fff;background:linear-gradient(180deg,#8a7e73,#4b4f56)}
.quote-mark{left:603px;top:2572px;width:42px;height:42px;background:var(--green);color:#fff;font-size:36px;font-weight:700;text-align:center;line-height:52px;font-family:Georgia,serif}
.testi-quote{left:692px;top:2544px;width:440px;font-size:14px;line-height:28px;color:#fff;font-style:italic}
.testi-meta{left:692px;top:2643px;font-size:12px;font-weight:700;color:#fff;display:flex;gap:14px}
.ctrl{top:2680px;width:44px;height:24px;background:#fff;display:flex;align-items:center;justify-content:center}

/* blog */
.blog-img{top:2976px;width:314px;height:206px}
.date{top:2976px;width:56px;height:56px;background:var(--teal);color:#fff;font-size:13px;font-weight:700;text-align:center;line-height:18px;padding-top:10px}
.tag{top:3204px;height:22px;background:var(--green);color:#fff;font-size:9px;font-weight:700;padding:0 16px;line-height:22px}
.blog-h{top:3246px;font-size:12.5px;font-weight:700;width:314px;padding-left:12px}
.blog-p{top:3273px;font-size:11.5px;line-height:18px;color:var(--grey);width:314px;padding-left:12px}
.blog-link{top:3322px;padding-left:12px}

/* contact */
.contact{top:3457px;left:0;width:1200px;height:555px;background:var(--teal)}
.frame{left:254px;top:3548px;width:692px;height:376px;border:2px solid #e8f3f1;border-radius:10px}
.contact h2{left:420px;top:3530px;width:360px;text-align:center;font-size:29px;color:#fff;background:var(--teal)}
.field{height:48px;background:var(--field);border-radius:3px;font-size:13px;color:#7a8a88;padding:15px 17px}
.submit{left:524px;top:3902px;width:151px;height:43px}

/* footer */
.footer{top:4012px;left:0;width:1200px;height:375px;background:var(--footer);color:#fff}
.foot-brand{left:132px;top:4160px;width:210px;display:flex;align-items:center;gap:10px;font-size:18px;font-weight:700}
.foot-brand i{width:22px;height:22px;border-radius:50%;background:#fff;display:block}
.foot-col h4{font-size:19px;font-weight:500;margin-bottom:14px}
.foot-col li{list-style:none;font-size:12.5px;line-height:31px;color:#ddd}
.foot-col .ic{display:inline-block;width:14px;margin-right:18px;text-align:center}
.copy{left:118px;top:4345px;font-size:12px;color:#ddd}
.social{top:4344px;width:16px;height:16px;border-radius:50%;background:#fff}
</style>
</head>
<body>
<div class="page">

  <!-- header -->
  <div class="abs topbar"><ul><li>HOME</li><li>ABOUT US</li><li>NEWS</li><li>TESTIMONIALS</li><li>CAREERS</li></ul></div>
  <div class="abs navbar"></div>
  <ul class="abs mainnav"><li>TREATMENTS</li><li>LOCATIONS</li><li>PHSICAL THERAPY</li><li>CULTURE</li><li>WELLNESS</li></ul>
  <div class="abs btn-appoint">REQUEST AN APPOINTMENT</div>

  <!-- hero -->
  <div class="abs hero" role="img" aria-label="Physical therapist helping a patient with a knee brace next to exercise balls"></div>
  <div class="abs logo-badge"><div class="dot"></div><span>CORWEN</span></div>
  <div class="abs hero-title display">CORWEN</div>
  <div class="abs hero-sub display">PHYSICAL THERAPY<br>&amp; WELLNESS</div>
  <p class="abs hero-text">Sed ut perspiciatis unde omnis iste natus error sit voluptatem accusantium doloremque laudantium, totam rem</p>
  <div class="abs btn" style="left:668px;top:496px;width:148px;height:44px">LEARN MORE <span class="arr"></span></div>

  <!-- features -->
  <div class="abs feature" style="left:108px;background:var(--teal)">
    <svg width="70" height="56" viewBox="0 0 70 56"><path d="M8 44 C8 20 30 12 46 14 C44 34 30 46 8 44Z M30 40 C36 24 52 18 64 22 C60 38 46 46 30 40Z" fill="#fff"/></svg>
    <h3>HOLISTIC APPROACH</h3><hr><p>Lorem ipsum dolor sit amet, consectetur adipiscing elit, sed do eiusmod tempor incidid</p>
  </div>
  <div class="abs feature" style="left:357px;background:var(--green)">
    <svg width="60" height="56" viewBox="0 0 60 56" fill="none" stroke="#fff" stroke-width="3"><circle cx="30" cy="28" r="20"/><path d="M30 8 L30 48 M10 28 L50 28 M16 14 L44 42 M44 14 L16 42"/></svg>
    <h3>ADVANCED TECHNOLOGY</h3><hr><p>Lorem ipsum dolor sit amet, consectetur adipiscing elit, sed do eiusmod tempor incidid</p>
  </div>
  <div class="abs feature" style="left:608px;background:var(--purple)">
    <svg width="60" height="56" viewBox="0 0 60 56"><circle cx="30" cy="26" r="15" fill="#fff"/><path d="M24 26 h12 M30 20 v12" stroke="var(--purple)" stroke-width="4"/><path d="M8 16 C8 40 20 50 30 52 C40 50 52 40 52 16" fill="none" stroke="#fff" stroke-width="4"/></svg>
    <h3>INTERDISCIPLINARY CARE</h3><hr><p>Lorem ipsum dolor sit amet, consectetur adipiscing elit, sed do eiusmod tempor incidid</p>
  </div>
  <div class="abs feature" style="left:858px;background:var(--green-dark)">
    <svg width="60" height="56" viewBox="0 0 60 56"><path d="M30 28 L20 18 A6 6 0 0 1 30 10 A6 6 0 0 1 40 18Z" fill="#fff"/><path d="M6 40 L22 36 L40 38 L54 30 L54 36 L38 48 L6 48Z" fill="#fff"/></svg>
    <h3>PERSONALIZED CARE</h3><hr><p>Lorem ipsum dolor sit amet, consectetur adipiscing elit, sed do eiusmod tempor incidid</p>
  </div>

  <!-- about -->
  <section class="abs about"></section>
  <h2 class="abs display" style="left:150px;top:1251px;font-size:29px;color:#fff">ABOUT US</h2>
  <p class="abs about-text">Sed ut perspiciatis unde omnis iste natus error sit voluptatem accusantium doloremque laudantium, totam rem aperiam, eaque ipsa quae ab illo inventore veritatis et quasi architecto beatae vitae dicta sunt explicabo. Nemo enim ipsam voluptatem quia voluptas sit aspernatur aut odit aut fugit, sed quia consequuntur magni dolores eos qui ratione voluptatem sequi nesciunt. Neque porro quisquam est, qui dolorem ipsum quia dolor sit amet, consectetur, adipisci velit, sed quia non numquam eius modi tempora incidunt ut labore et dolore magnam aliquam quaerat voluptatem. Ut enim ad minima</p>
  <div class="abs btn green" style="left:150px;top:1552px;width:150px;height:40px">LEARN MORE <span class="arr"></span></div>
  <div class="abs about-photo" role="img" aria-label="Older man and young woman giving a high five during exercise"></div>

  <!-- services -->
  <h2 class="abs sec-title display" style="top:1767px">OUR SERVICES</h2>
  <div class="abs svc-img" style="left:112px;background:linear-gradient(135deg,#d9e3e6,#a6bcc4 60%,#7f97a3)" role="img" aria-label="Therapist treating a patient's leg on a mat"></div>
  <div class="abs svc-img" style="left:608px;background:linear-gradient(180deg,#a7c38a,#6f9a4e 55%,#4c7a2f)" role="img" aria-label="Group doing outdoor fitness exercises on grass"></div>
  <svg class="abs" style="left:112px;top:2100px" width="478" height="52" viewBox="0 0 478 52"><path d="M0 40 L240 0 L478 52 L478 24 L240 10 L0 52Z" fill="var(--green)"/><path d="M0 52 L240 12 L478 52Z" fill="#fff"/></svg>
  <svg class="abs" style="left:608px;top:2100px" width="478" height="52" viewBox="0 0 478 52"><path d="M0 40 L240 0 L478 52 L478 24 L240 10 L0 52Z" fill="var(--green)"/><path d="M0 52 L240 12 L478 52Z" fill="#fff"/></svg>
  <h3 class="abs svc-title display" style="left:112px">PHYSICAL THERAPY</h3>
  <h3 class="abs svc-title display" style="left:608px">WELLNESS</h3>
  <p class="abs svc-text" style="left:112px">Sed ut perspiciatis unde omnis iste natus error sit voluptatem accusantium doloremque laudantium, totam rem aperiam, eaque ipsa quae ab illo inventore veritatis et quasi architecto</p>
  <p class="abs svc-text" style="left:608px">Sed ut perspiciatis unde omnis iste natus error sit voluptatem accusantium doloremque laudantium, totam rem aperiam, eaque ipsa quae ab illo inventore veritatis et quasi architecto</p>
  <span class="abs link" style="left:312px;top:2295px">LEARN MORE</span>
  <span class="abs link" style="left:808px;top:2295px">LEARN MORE</span>

  <!-- testimonials -->
  <section class="abs testi" role="img" aria-label="Dimmed background of a patient receiving treatment"></section>
  <h2 class="abs display" style="left:112px;top:2532px;font-size:30px;line-height:38px;color:#fff">WHAT OUR<br>CLIENTS SAY</h2>
  <p class="abs testi-lead">Lorem ipsum dolor sit amet, consectetur adipiscing elit, sed do eiusmod tempor incididunt ut labore et dolore</p>
  <div class="abs testi-photo" role="img" aria-label="Portrait of a smiling client in a suit"></div>
  <div class="abs quote-mark">&#8220;</div>
  <p class="abs testi-quote">" Sed ut perspiciatis unde omnis iste natus error sit voluptatem accusantium doloremque laudantium, totam rem aperiam, eaque ipsa quae ab illo inventore veritatis et "</p>
  <div class="abs testi-meta"><span>DALE HARMON</span><span>|</span><span>ONLINE REVIEW</span><span>|</span><span style="letter-spacing:2px">★★★★★</span></div>
  <div class="abs ctrl" style="left:692px"><svg width="22" height="10"><path d="M2 5 H20 M2 5 L7 1 M2 5 L7 9" stroke="#222" stroke-width="2" fill="none"/></svg></div>
  <div class="abs ctrl" style="left:744px"><svg width="22" height="10"><path d="M2 5 H20 M20 5 L15 1 M20 5 L15 9" stroke="#222" stroke-width="2" fill="none"/></svg></div>

  <!-- blog -->
  <h2 class="abs sec-title display" style="top:2904px">RECENT BLOG</h2>
  <div class="abs blog-img" style="left:108px;background:linear-gradient(135deg,#d8dde0,#98a6b2)" role="img" aria-label="Trainer assisting a woman with an arm stretch"></div>
  <div class="abs blog-img" style="left:443px;background:linear-gradient(135deg,#eef0ee,#b9c0bd)" role="img" aria-label="Man exercising with a resistance band indoors"></div>
  <div class="abs blog-img" style="left:778px;background:linear-gradient(135deg,#f1efe9,#c6c9bf)" role="img" aria-label="Couple stretching their arms together"></div>
  <div class="abs date" style="left:357px">SEP<br>2021</div>
  <div class="abs date" style="left:692px">SEP<br>2021</div>
  <div class="abs date" style="left:1027px">SEP<br>2021</div>
  <div class="abs tag" style="left:120px">WELLNESS</div>
  <div class="abs tag" style="left:455px">PHYSICAL THERAPY</div>
  <div class="abs tag" style="left:790px">WELLNESS</div>
  <h4 class="abs blog-h" style="left:108px">LOREM IPSUM DOLOR SIT AMET, CONSEC</h4>
  <h4 class="abs blog-h" style="left:443px">LOREM IPSUM DOLOR SIT AMET, CONSEC</h4>
  <h4 class="abs blog-h" style="left:778px">LOREM IPSUM DOLOR SIT AMET, CONSEC</h4>
  <p class="abs blog-p" style="left:108px">Sed ut perspiciatis unde omnis iste natus error sit<br>voluptatem accusantium doloremque</p>
  <p class="abs blog-p" style="left:443px">Sed ut perspiciatis unde omnis iste natus error sit<br>voluptatem accusantium doloremque</p>
  <p class="abs blog-p" style="left:778px">Sed ut perspiciatis unde omnis iste natus error sit<br>voluptatem accusantium doloremque</p>
  <span class="abs link blog-link" style="left:108px">LEARN MORE ➜</span>
  <span class="abs link blog-link" style="left:443px">LEARN MORE ➜</span>
  <span class="abs link blog-link" style="left:778px">LEARN MORE ➜</span>

  <!-- contact -->
  <section class="abs contact"></section>
  <div class="abs frame"></div>
  <h2 class="abs display" style="left:420px;top:3530px;width:360px;text-align:center;font-size:29px;color:#fff;background:var(--teal)">GET IN TOUCH</h2>
  <div class="abs field" style="left:307px;top:3618px;width:289px">Full name</div>
  <div class="abs field" style="left:608px;top:3618px;width:289px">Email</div>
  <div class="abs field" style="left:307px;top:3679px;width:289px">Phone No</div>
  <div class="abs field" style="left:608px;top:3679px;width:289px">Company</div>
  <div class="abs field" style="left:307px;top:3739px;width:590px;height:110px">Message</div>
  <div class="abs btn green submit">SUBMIT NOW <span class="arr"></span></div>

  <!-- footer -->
  <footer class="abs footer"></footer>
  <div class="abs foot-brand"><i></i>CORWEN</div>
  <div class="abs foot-col" style="left:426px;top:4064px"><h4>Site Map</h4><ul><li>Home</li><li>About Us</li><li>Our Services</li><li>Blog</li><li>Contact Us</li></ul></div>
  <div class="abs foot-col" style="left:608px;top:4064px"><h4>Other Links</h4><ul><li>FAQ</li><li>Terms Of Use</li><li>Privacy Policy</li><li>Reviews</li><li>Physical Therapy</li></ul></div>
  <div class="abs foot-col" style="left:806px;top:4064px"><h4>Contact Us</h4><ul>
    <li>418 Birchwood Lane, Millbrook</li><li>United States</li>
    <li><span class="ic">&#9742;</span>1 555 010 0199</li>
    <li><span class="ic">&#9993;</span>info@corwenphysicaltherapy.com</li>
    <li><span class="ic">&#9719;</span>Mon-Fri: 8:00 a.m. – 5:00 p.m</li></ul></div>
  <p class="abs copy">© Copyright 2021 Corwen Physical Therapy.  All Right Reserved</p>
  <span class="abs social" style="left:935px"></span>
  <span class="abs social" style="left:965px"></span>
  <span class="abs social" style="left:995px"></span>
  <span class="abs social" style="left:1025px"></span>
  <span class="abs social" style="left:1055px"></span>
</div>
</body>
</html>
```